Bref créative
Harbor Floors & More --- Business card
Harbor Floors & More - thousands of types of tiles
Simple
Mei Dalton
4150 Marwood Ave,
Unit 3B, Concord, ON
L4K 5R8
mei.dalton@harborfloorsmore.example
www.harborfloorsmore.example
Introduction : Harbor Floors & More imports and distributes thousands of types of tiles in limestone, marble, slate, granite, porcelan, ceramic, glass and aluminum for homeowners, builders and contractors. Also providing custom-made solid wood kitchen cabinet and vanities.
the logo of Harbor Floors & More
Logo on Black
Logo on White

```html
<!DOCTYPE html>
<html lang="en">
<head>
<meta charset="utf-8">
<title>Harbor Floors &amp; More — Stationery</title>
<link href="https://fonts.googleapis.com/css2?family=Open+Sans:wght@400;600&display=swap" rel="stylesheet">
<style>
  :root {
    --bg: #e9eaec;
    --paper: #ffffff;
    --green: #a3c414;
    --green-light: #cfe04a;
    --green-dark: #7fa10c;
    --ink: #3b3f44;
    --muted: #7a7e84;
    --faint: #e4ecc4;
  }
  * { margin: 0; padding: 0; box-sizing: border-box; }
  html, body { width: 1200px; height: 936px; overflow: hidden; }
  body {
    background: var(--bg);
    font-family: "Open Sans", Arial, sans-serif;
    color: var(--ink);
    position: relative;
  }
  .sheet {
    position: absolute;
    background: var(--paper);
    overflow: hidden;
    box-shadow: 0 2px 6px rgba(0,0,0,.12);
  }
  .sheet svg.swoosh { position: absolute; inset: 0; width: 100%; height: 100%; }
  .brand {
    position: absolute;
    display: flex;
    align-items: center;
    gap: 8px;
    font-weight: 600;
    color: var(--ink);
    white-space: nowrap;
    letter-spacing: .01em;
    z-index: 1;
  }
  .brand .mark { background: var(--green); flex: none; }

  /* Letterhead */
  .letterhead { left: 182px; top: 71px; width: 395px; height: 549px; }
  .letterhead .brand { left: 26px; top: 32px; font-size: 13px; }
  .letterhead .brand .mark { width: 12px; height: 12px; }
  .letterhead .contact {
    position: absolute; left: 246px; top: 24px;
    font-size: 6px; line-height: 9.5px; color: var(--muted);
  }
  .letterhead .contact span::before {
    content: ""; display: inline-block; width: 5px; height: 5px;
    border-radius: 50%; background: var(--green); margin-right: 4px; vertical-align: -0.5px;
  }
  .letterhead .watermark {
    position: absolute; left: 0; right: 0; top: 250px;
    text-align: center; font-size: 28px; font-weight: 600; color: var(--faint);
  }

  /* Folder */
  .folder { left: 632px; top: 56px; width: 393px; height: 559px; }
  .folder .brand {
    left: 40px; right: 0; top: 300px;
    justify-content: center;
    font-size: 22px; gap: 10px;
  }
  .folder .brand .mark { width: 22px; height: 22px; }

  /* Business cards */
  .card-front { left: 43px; top: 663px; width: 195px; height: 99px; }
  .card-front .person { position: absolute; left: 12px; top: 10px; font-size: 6px; line-height: 8px; color: var(--muted); }
  .card-front .person b { font-weight: 600; color: var(--ink); }
  .card-front .brand { left: 12px; top: 32px; font-size: 7px; gap: 4px; }
  .card-front .brand .mark { width: 7px; height: 7px; }
  .card-back { left: 43px; top: 777px; width: 195px; height: 101px; background: var(--green); }
  .card-back .site { position: absolute; left: 0; right: 0; bottom: 10px; text-align: center; font-size: 5.5px; color: #fff; }

  /* Envelopes */
  .envelope-front { left: 261px; top: 663px; width: 445px; height: 210px; }
  .envelope-front .brand { left: 36px; top: 36px; font-size: 14px; }
  .envelope-front .brand .mark { width: 14px; height: 14px; }
  .envelope-front .address { position: absolute; left: 36px; top: 62px; font-size: 6.5px; color: var(--muted); }
  .envelope-back { left: 734px; top: 663px; width: 430px; height: 210px; }
  .envelope-back .site { position: absolute; left: 0; right: 0; top: 15px; text-align: center; font-size: 7px; color: #fff; letter-spacing: .03em; }
</style>
</head>
<body>

<section class="sheet letterhead">
  <div class="brand"><span class="mark"></span>Harbor Floors &amp; More</div>
  <div class="contact">
    <span>4150 Marwood Ave, Unit 3B</span><br>
    <span>Concord, ON L4K 5R8</span><br>
    <span>Tel 905 555 0142</span><br>
    <span>mei.dalton@harborfloorsmore.example</span><br>
    <span>www.harborfloorsmore.example</span>
  </div>
  <div class="watermark">Harbor Floors &amp; More</div>
  <svg class="swoosh" viewBox="0 0 395 549" preserveAspectRatio="none" aria-hidden="true">
    <defs><linearGradient id="lhG" x1="0" x2="1"><stop offset="0" stop-color="var(--green-dark)"/><stop offset="1" stop-color="var(--green-light)"/></linearGradient></defs>
    <path d="M0 549 L0 536 C120 534 250 520 395 470 L395 549 Z" fill="url(#lhG)"/>
    <path d="M0 530 C130 528 260 512 395 462" fill="none" stroke="var(--green)" stroke-width="1"/>
  </svg>
</section>

<section class="sheet folder">
  <svg class="swoosh" viewBox="0 0 393 559" preserveAspectRatio="none" aria-hidden="true">
    <defs><linearGradient id="fdG" x1="0" y1="0" x2="0" y2="1"><stop offset="0" stop-color="var(--green-light)"/><stop offset="1" stop-color="var(--green-dark)"/></linearGradient></defs>
    <path d="M0 0 L12 0 C40 90 30 170 16 260 C4 350 20 460 62 559 L0 559 Z" fill="url(#fdG)"/>
    <path d="M20 0 C48 95 38 175 24 262 C12 352 28 460 70 559" fill="none" stroke="var(--green)" stroke-width="1"/>
  </svg>
  <div class="brand"><span class="mark"></span>Harbor Floors &amp; More</div>
</section>

<section class="sheet card-front">
  <div class="person"><b>Mei Dalton</b><br>Sales Manager</div>
  <div class="brand"><span class="mark"></span>Harbor Floors &amp; More</div>
  <svg class="swoosh" viewBox="0 0 195 99" preserveAspectRatio="none" aria-hidden="true">
    <path d="M0 99 L0 72 C70 76 140 74 195 58 L195 99 Z" fill="var(--green)"/>
    <path d="M0 68 C70 72 140 70 195 54" fill="none" stroke="var(--green-light)" stroke-width="1"/>
  </svg>
</section>

<section class="sheet card-back">
  <svg class="swoosh" viewBox="0 0 195 101" preserveAspectRatio="none" aria-hidden="true">
    <path d="M0 70 C70 74 140 70 195 52" fill="none" stroke="#fff" stroke-width="1.2"/>
    <path d="M0 76 C70 80 140 76 195 58" fill="none" stroke="var(--green-light)" stroke-width="1"/>
  </svg>
  <div class="site">www.harborfloorsmore.example</div>
</section>

<section class="sheet envelope-front">
  <div class="brand"><span class="mark"></span>Harbor Floors &amp; More</div>
  <div class="address">4150 Marwood Ave, Unit 3B, Concord, ON L4K 5R8</div>
  <svg class="swoosh" viewBox="0 0 445 210" preserveAspectRatio="none" aria-hidden="true">
    <path d="M445 150 C420 185 395 200 360 210 L445 210 Z" fill="var(--green)"/>
  </svg>
</section>

<section class="sheet envelope-back">
  <svg class="swoosh" viewBox="0 0 430 210" preserveAspectRatio="none" aria-hidden="true">
    <path d="M0 0 L430 0 L430 40 C300 52 130 52 0 40 Z" fill="var(--green)"/>
    <path d="M0 48 C130 60 300 60 430 48" fill="none" stroke="var(--green-light)" stroke-width="1"/>
    <path d="M0 40 L215 150 L430 40" fill="none" stroke="#dcdde0" stroke-width="1"/>
    <path d="M0 210 L190 130 M430 210 L240 130" fill="none" stroke="#e6e7ea" stroke-width="1"/>
  </svg>
  <div class="site">www.harborfloorsmore.example</div>
</section>

</body>
</html>
```